Redesign Colorful Business Card

Please redesign the card attached. It is too busy. Please don't eliminate any of the words. The repetivite word "free" can be used less often.

Target Market(s)

College Students.

Contact Information for Business Card

The details listed in the attached image

Font styles to use
Sans Serif

Requirements
Must have
• A clear and simple presentation and must be attractive.

```html
<!DOCTYPE html>
<html lang="en">
<head>
<meta charset="utf-8">
<title>StudyNimbl.com – Business Card</title>
<link rel="stylesheet" href="https://fonts.googleapis.com/css2?family=Arimo:wght@400;700&family=Montserrat:ital,wght@0,900;1,900&display=swap">
<style>
  :root {
    --page-bg: #e9e9ee;
    --navy: #0b1a3a;
    --periwinkle: #8c8cf2;
    --lavender: #ececf8;
    --teal: #1ba9c6;
    --yellow: #f5cf2f;
    --red: #e23d36;
    --white: #ffffff;
    --text-dark: #14204a;
  }
  * { box-sizing: border-box; margin: 0; padding: 0; }
  html, body {
    width: 1200px; height: 1200px; overflow: hidden;
    background: var(--page-bg);
  }
  .card {
    position: absolute; left: 60px; top: 221px;
    width: 1080px; height: 759px; overflow: hidden;
    background: var(--lavender);
    font-family: "Arimo", Arial, sans-serif;
    color: var(--text-dark);
  }
  .card-shapes { position: absolute; inset: 0; width: 100%; height: 100%; }
  .art { position: absolute; border-radius: 14px; }
  .art--time-cut {
    left: 16px; top: 22px; width: 286px; height: 176px;
    background: linear-gradient(135deg, rgba(245,207,47,.55), rgba(226,92,74,.45));
  }
  .art--online-class {
    left: 452px; top: 243px; width: 266px; height: 180px;
    background: linear-gradient(160deg, #dcdff0, #9aa3c8 60%, #e8a79c);
  }
  .art--mind {
    left: 790px; top: 146px; width: 280px; height: 160px;
    background: linear-gradient(180deg, rgba(255,255,255,.12), rgba(242,139,139,.45));
  }
  .tagline {
    position: absolute; left: 377px; top: 62px;
    font-weight: 700; font-size: 29px; line-height: 39px; text-transform: uppercase;
  }
  .study-time {
    position: absolute; left: 0; top: 247px; width: 355px; text-align: center;
    font-weight: 700; font-size: 27px; line-height: 38px; text-transform: uppercase;
  }
  .study-time__figure {
    display: block; margin-top: 8px;
    font-size: 68px; line-height: 76px; color: var(--white);
  }
  .free-badge {
    position: absolute; left: 777px; top: 12px;
    font-family: "Montserrat", Arial, sans-serif; font-weight: 900;
    font-size: 60px; letter-spacing: 3px; color: var(--yellow);
  }
  .free-badge__marks { color: var(--red); letter-spacing: 1px; }
  .memorize {
    position: absolute; color: var(--white); font-weight: 700; text-transform: uppercase;
    font-size: 29px; line-height: 34px;
  }
  .memorize--line1 { left: 758px; top: 324px; }
  .memorize--line2 { left: 868px; top: 363px; }
  .memorize--accent {
    left: 790px; top: 396px;
    font-family: "Montserrat", Arial, sans-serif; font-weight: 900; font-style: italic;
    font-size: 44px; line-height: 54px;
  }
  .brand {
    position: absolute; left: 200px; top: 590px;
    display: flex; align-items: center; gap: 24px;
  }
  .brand__mark { width: 46px; height: 46px; background: var(--periwinkle); }
  .brand__name {
    font-family: "Arimo", Arial, sans-serif; font-weight: 400;
    font-size: 74px; line-height: 1; color: var(--white);
  }
  .copyright {
    position: absolute; left: 282px; top: 676px; width: 514px; height: 48px;
    border-radius: 24px; background: var(--periwinkle);
    display: flex; flex-direction: column; justify-content: center; align-items: center;
    font-weight: 700; font-size: 17px; line-height: 20px; color: var(--navy);
  }
</style>
</head>
<body>
  <main class="card">
    <svg class="card-shapes" viewBox="0 0 830 583" preserveAspectRatio="none" aria-hidden="true">
      <rect class="panel-left" x="0" y="0" width="273" height="440" fill="var(--periwinkle)"/>
      <path class="header-wave" d="M405,0 H830 V88 H610 C560,88 520,72 490,45 C462,18 440,0 405,0Z" fill="var(--navy)"/>
      <rect class="panel-right" x="557" y="88" width="273" height="440" fill="var(--teal)"/>
      <line class="accent-rule" x1="690" y1="352" x2="830" y2="352" stroke="var(--white)" stroke-width="2"/>
      <line class="accent-rule" x1="676" y1="364" x2="830" y2="364" stroke="var(--white)" stroke-width="2"/>
      <path class="footer-edge" d="M0,400 C150,340 350,322 480,328 C640,345 780,420 830,492 V583 H0Z" fill="var(--lavender)"/>
      <path class="footer-band" d="M0,417 C150,357 350,339 480,345 C640,362 780,437 830,509 V583 H0Z" fill="var(--navy)"/>
    </svg>

    <div class="art art--time-cut" role="img" aria-label="Illustration of an alarm clock with scissors cutting time"></div>
    <div class="art art--online-class" role="img" aria-label="Illustration of a student joining an online class on a computer"></div>
    <div class="art art--mind" role="img" aria-label="Illustration of a person steering a large brain"></div>

    <p class="tagline">Learn<br>a subject<br>without having<br>to go to class</p>

    <p class="study-time">Cut study time<br>down by up to<span class="study-time__figure">50%</span></p>

    <p class="free-badge">FREE<span class="free-badge__marks">!!!</span></p>

    <p class="memorize memorize--line1">Memorize</p>
    <p class="memorize memorize--line2">Anything</p>
    <p class="memorize memorize--accent">QUICKLY!</p>

    <div class="brand">
      <span class="brand__mark"></span>
      <span class="brand__name">StudyNimbl.com</span>
    </div>

    <p class="copyright"><span>Copyright Nimbl Services, LLC 2013-2022</span><span>All Rights Reserved</span></p>
  </main>
</body>
</html>
```